New business card for UK roofing company

We are Penwick Roofing and we need a business card design for our staff.

We offer the following services:

- New roofs
- General roof repairs
- Drone surveys
- Single ply roofing
- Steel cladding
- Asbestos removal
- Electronic leak detection

I have attached our logo. I have also attached example branding printed to our vans. The business card should fit in with the style of our branding.

The business card should have the following information;

Address:
Unit 17c Marlow Dene Farm
Marlow Dene Lane
Fenbury
RX4 9QD

Telephone: 020 7946 0312
24 Hour: 0800 471 9062

Email: tom@penwickroofing.com
Mobile: 07700900418
Name: Tom Harley
Website: www.penwickroofing.com

The business card will be printed in Spot UV, see here: https://www.printvane.com/business-cards/spot-uv/

If you need anymore info, please let me know,

```html
<!DOCTYPE html>
<html lang="en">
<head>
<meta charset="utf-8">
<title>Penwick Roofing – Business Card</title>
<link href="https://fonts.googleapis.com/css2?family=Archivo:wght@400;500;700;800;900&display=swap" rel="stylesheet">
<style>
  :root {
    --sky: #12b0dd;
    --navy: #0a4a7a;
    --white: #ffffff;
    --font: "Archivo", "Helvetica Neue", Arial, sans-serif;
  }
  * { margin: 0; padding: 0; box-sizing: border-box; }
  html, body { width: 1200px; height: 1200px; overflow: hidden; }
  body { background: var(--sky); font-family: var(--font); position: relative; }

  .card { position: absolute; left: 172px; width: 857px; height: 490px; overflow: hidden; background: var(--white); }
  .card--front { top: 63px; }
  .card--back { top: 621px; }
  .card__shape { position: absolute; inset: 0; width: 100%; height: 100%; }

  /* Front */
  .brand { position: absolute; left: 56px; top: 64px; display: flex; align-items: center; gap: 14px; }
  .brand__dot { width: 58px; height: 58px; border-radius: 50%; background: var(--sky); }
  .brand__name { font-size: 50px; font-weight: 800; color: var(--navy); letter-spacing: -1.5px; line-height: 1; white-space: nowrap; }

  .services { position: absolute; left: 56px; top: 137px; list-style: none; color: var(--navy); font-size: 23px; line-height: 27.5px; white-space: nowrap; }
  .services li { position: relative; padding-left: 26px; }
  .services li::before { content: ""; position: absolute; left: 0; top: 10px; width: 10px; height: 10px; border-radius: 50%; background: var(--navy); }

  .badge { position: absolute; left: 622px; top: 178px; width: 164px; height: 170px; }
  .badge__text { position: absolute; left: 622px; top: 222px; width: 164px; text-align: center; color: var(--white); font-weight: 900; line-height: 1; }
  .badge__num { font-size: 56px; letter-spacing: -2px; }
  .badge__hour { font-size: 25px; margin-top: 1px; }
  .badge__service { font-size: 17px; letter-spacing: 0.2px; }

  .front-contact { position: absolute; right: 79px; color: var(--white); display: flex; align-items: center; line-height: 1; white-space: nowrap; }
  .front-contact--phone { top: 366px; font-size: 44px; gap: 14px; }
  .front-contact--web { top: 421px; font-size: 32px; gap: 18px; letter-spacing: -0.3px; }

  /* Back */
  .name-bar { position: absolute; left: 0; top: 77px; width: 53px; height: 29px; background: var(--sky); }
  .person { position: absolute; left: 61px; top: 70px; text-align: right; white-space: nowrap; }
  .person__name { font-size: 40px; font-weight: 900; color: var(--navy); line-height: 1; letter-spacing: 0.3px; text-align: left; }
  .person__role { font-size: 23px; color: var(--sky); margin-top: 6px; line-height: 1; }

  .contact { position: absolute; left: 59px; display: flex; align-items: center; gap: 20px; color: var(--navy); font-size: 22px; line-height: 28.5px; white-space: nowrap; }
  .contact__icon { width: 32px; flex: none; display: flex; justify-content: center; }
  .contact__address { font-style: normal; }
  .contact--address { top: 165px; }
  .contact--phone { top: 266px; }
  .contact--email { top: 344px; }
  .contact--web { top: 404px; }

  .tagline { position: absolute; left: 466px; width: 400px; top: 76px; text-align: center; color: var(--white); font-size: 20px; font-weight: 500; letter-spacing: 0.8px; }
  .back-brand__dot { position: absolute; left: 629px; top: 158px; width: 74px; height: 74px; border-radius: 50%; background: var(--sky); }
  .back-brand__name { position: absolute; left: 466px; width: 400px; top: 258px; text-align: center; color: var(--white); font-size: 38px; font-weight: 800; letter-spacing: -1px; line-height: 1; white-space: nowrap; }
</style>
</head>
<body>

<section class="card card--front">
  <svg class="card__shape" viewBox="0 0 1379 788" preserveAspectRatio="none" aria-hidden="true">
    <path fill="var(--navy)" d="M1169 0 H1379 V788 H0 C500 670 950 400 1169 0 Z"/>
    <path fill="var(--sky)" d="M1069 0 H1169 C950 400 500 670 0 788 V762 C450 650 880 420 1069 0 Z"/>
  </svg>

  <div class="brand">
    <span class="brand__dot"></span>
    <span class="brand__name">Penwick Roofing</span>
  </div>

  <ul class="services">
    <li>New Roofs</li>
    <li>General roof repairs</li>
    <li>Drone roof surveys</li>
    <li>Single ply roofing</li>
    <li>Steel cladding</li>
    <li>Asbestos removal</li>
    <li>Electronic leak detection</li>
  </ul>

  <svg class="badge" viewBox="0 0 164 170" aria-hidden="true">
    <path d="M149 59 A74 74 0 1 1 122 28" fill="none" stroke="var(--white)" stroke-width="6"/>
    <path d="M136 38 L126 18 L114 35 Z" fill="var(--white)"/>
  </svg>
  <div class="badge__text">
    <div class="badge__num">24</div>
    <div class="badge__hour">HOUR</div>
    <div class="badge__service">SERVICE</div>
  </div>

  <div class="front-contact front-contact--phone">
    <svg width="34" height="34" viewBox="0 0 24 24" aria-hidden="true"><path fill="var(--white)" d="M6.6 2.5 9.3 6.4 7.4 8.6c1.2 2.6 3.3 4.8 6 6l2.2-1.9 3.9 2.7-1.6 3.4c-8.3-.4-14.6-6.8-15-15Z"/></svg>
    <span>0800 471 9062</span>
  </div>
  <div class="front-contact front-contact--web">
    <svg width="32" height="32" viewBox="0 0 24 24" aria-hidden="true"><circle cx="12" cy="12" r="11" fill="var(--white)"/><path d="M3 9l9 3 8-6M5 18l7-6 5 9M12 12l9 2" stroke="var(--navy)" stroke-width="1.2" fill="none"/></svg>
    <span>www.penwickroofing.com</span>
  </div>
</section>

<section class="card card--back">
  <svg class="card__shape" viewBox="0 0 1379 788" preserveAspectRatio="none" aria-hidden="true">
    <path fill="var(--sky)" d="M652 0 H1379 V788 H865 C720 600 665 400 652 0 Z"/>
    <path fill="var(--navy)" d="M692 0 H1379 V788 H976 C800 620 705 380 692 0 Z"/>
  </svg>

  <div class="name-bar"></div>
  <div class="person">
    <div class="person__name">TOM HARLEY</div>
    <div class="person__role">Founder/CEO</div>
  </div>

  <div class="contact contact--address">
    <span class="contact__icon"><svg width="30" height="38" viewBox="0 0 24 30" aria-hidden="true"><path d="M12 2a9 9 0 0 0-9 9c0 6 9 16 9 16s9-10 9-16a9 9 0 0 0-9-9Z" fill="none" stroke="var(--navy)" stroke-width="3.2"/><circle cx="12" cy="11" r="3.4" fill="var(--navy)"/></svg></span>
    <address class="contact__address">Unit 17c Marlow Dene Farm<br>Marlow Dene Lane,Fenbury<br>RX4 9QD</address>
  </div>

  <div class="contact contact--phone">
    <span class="contact__icon"><svg width="38" height="34" viewBox="0 0 38 34" aria-hidden="true"><path d="M2 10c0-6 34-6 34 0v3h-8v-3H10v3H2Z" fill="var(--navy)"/><path d="M8 15h22l4 6v11H4V21Z" fill="var(--navy)"/><circle cx="19" cy="23" r="5" fill="none" stroke="var(--white)" stroke-width="2.2"/></svg></span>
    <div>020 7946 0312<br>07700900418</div>
  </div>

  <div class="contact contact--email">
    <span class="contact__icon"><svg width="34" height="32" viewBox="0 0 34 32" aria-hidden="true"><path d="M1 2 33 17 14 19Z" fill="var(--navy)"/><path d="M14 19l4 11 3-9" fill="var(--navy)"/></svg></span>
    <span>tom@penwickroofing.com</span>
  </div>

  <div class="contact contact--web">
    <span class="contact__icon"><svg width="32" height="32" viewBox="0 0 24 24" aria-hidden="true"><circle cx="12" cy="12" r="11" fill="var(--navy)"/><path d="M3 9l9 3 8-6M5 18l7-6 5 9M12 12l9 2" stroke="var(--white)" stroke-width="1.2" fill="none"/></svg></span>
    <span>www.penwickroofing.com</span>
  </div>

  <div class="tagline">Your Local Roofing Expert</div>
  <div class="back-brand__dot"></div>
  <div class="back-brand__name">Penwick Roofing</div>
</section>

</body>
</html>
```